We need visit card and a letter paper for our website. thx

We have a beauty clinic in Switzerland.
https://wiesentalblick.ch
We need a visit card.

Requirements
Must have
• see colors on website

```html
<!DOCTYPE html>
<html lang="de">
<head>
<meta charset="utf-8">
<title>Wiesentalblick – Visitenkarte</title>
<link rel="stylesheet" href="https://fonts.googleapis.com/css2?family=Montserrat:wght@400;600;700&family=Arimo:wght@400&display=swap">
<style>
  :root {
    --stage: #d9d9db;
    --card-dark: #000000;
    --panel-dark: #0b0b0b;
    --card-light: #ffffff;
    --ink-light: #ffffff;
    --ink-dark: #111111;
    --ink-muted: #cfcfcf;
    --rule: #8a8a8a;
  }
  * { box-sizing: border-box; margin: 0; padding: 0; }
  html, body { width: 1200px; height: 900px; overflow: hidden; }
  body { background: var(--stage); position: relative; font-family: "Arimo", Arial, sans-serif; }

  .card {
    position: absolute;
    width: 520px;
    height: 300px;
    border-radius: 28px;
    box-shadow: 0 6px 18px rgba(0,0,0,.18);
    overflow: hidden;
  }

  /* Front */
  .card--front { left: 70px; top: 130px; background: var(--card-dark); }
  .front__panel {
    position: absolute; left: 50px; top: 45px; width: 420px; height: 210px;
    background: var(--panel-dark);
    display: flex; flex-direction: column; align-items: center; justify-content: center; gap: 22px;
  }
  .front__brand {
    font-family: "Montserrat", Arial, sans-serif; font-weight: 600;
    font-size: 38px; color: var(--ink-light); letter-spacing: .5px;
  }
  .front__url {
    font-family: "Montserrat", Arial, sans-serif; font-weight: 400;
    font-size: 13px; color: var(--ink-muted); letter-spacing: 3px;
  }

  /* Back */
  .card--back { left: 610px; top: 450px; background: var(--card-light); color: var(--ink-dark); }
  .back__brand {
    position: absolute; right: 40px; top: 56px;
    font-family: "Montserrat", Arial, sans-serif; font-weight: 600;
    font-size: 28px; color: var(--ink-dark);
  }
  .back__doctors {
    position: absolute; left: 40px; top: 160px;
    font-family: "Montserrat", Arial, sans-serif; font-weight: 700; font-size: 14px;
  }
  .back__doctors .title { font-weight: 400; }
  .back__address {
    position: absolute; right: 40px; top: 120px; text-align: right;
    font-size: 13px; line-height: 1.4;
  }
  .back__contacts {
    position: absolute; left: 40px; top: 200px; list-style: none;
    font-size: 14px; line-height: 1.5;
  }
  .back__contacts li { display: flex; align-items: center; gap: 8px; }
  .icon { width: 16px; height: 16px; flex: none; }
</style>
</head>
<body>

<section class="card card--front" aria-label="Visitenkarte Vorderseite">
  <div class="front__panel">
    <div class="front__brand">Wiesentalblick</div>
    <div class="front__url">www.wiesentalblick.ch</div>
  </div>
</section>

<section class="card card--back" aria-label="Visitenkarte Rückseite">
  <div class="back__brand">Wiesentalblick</div>

  <address class="back__address" style="font-style:normal">
    Talweg 24<br>
    7550 Scuol, Switzerland
  </address>

  <p class="back__doctors">Dr. Lena Vogt &amp; Dr. Marco Brunner<span class="title">, DESA</span></p>

  <ul class="back__contacts">
    <li>
      <svg class="icon" viewBox="0 0 16 16" aria-hidden="true">
        <rect x="1" y="1" width="14" height="14" rx="1.5" fill="none" stroke="currentColor" stroke-width="1.4"/>
        <path d="M5 4.5l1.5-.5 1 2-1 .8c.5 1 1.2 1.7 2.2 2.2l.8-1 2 1-.5 1.5c-3 0-6-3-6-6z" fill="currentColor"/>
      </svg>
      +41 (0) 800 20 30 40
    </li>
    <li>
      <svg class="icon" viewBox="0 0 16 16" aria-hidden="true">
        <rect x="1" y="3" width="14" height="10" fill="currentColor"/>
        <path d="M1 3l7 6 7-6" fill="none" stroke="#fff" stroke-width="1.2"/>
      </svg>
      hallo@wiesentalblick.ch
    </li>
    <li>
      <svg class="icon" viewBox="0 0 16 16" aria-hidden="true">
        <circle cx="8" cy="8" r="7" fill="currentColor"/>
        <path d="M1 8h14M8 1c-3 3.5-3 10.5 0 14M8 1c3 3.5 3 10.5 0 14" fill="none" stroke="#fff" stroke-width="1"/>
      </svg>
      www.wiesentalblick.ch
    </li>
  </ul>
</section>

</body>
</html>
```